Business card representing 2 natural foods companies!

Would love a business card that represents the 2 companies that I manage, PulpNova and Mirefield Crisp Leaf Co. Clearly, they are both premium food brands that have a cool, modern but classic feel.
I'm open to ideas for how to represent on 1 business card that I am Founder and President of both companies.
Contact Information for Business Card
Logos for both brands, and I think the most important thing is 2 different websites for each company (and perhaps 2 different emails for both companies)
sippulpnova.example
tobin@sippulpnova.example
mirefieldcrispleaf.example
tobin@mirefieldcrispleaf.example
Address isn't needed. I think phone number is good:
just cell: 555-014-7738
Also thinking is it possible to include a black LinkedIn QR code? I think that would be really cool to include.
Look and feel
Each slider illustrates characteristics of the customer's brand and the style your logo design should communicate.

```html
<!DOCTYPE html>
<html lang="en">
<head>
<meta charset="utf-8">
<title>PulpNova &amp; Mirefield Crisp Leaf Co. — Business Cards</title>
<link rel="stylesheet" href="https://fonts.googleapis.com/css2?family=Lato:wght@400;700;900&family=Playfair+Display:wght@700&display=swap">
<style>
  :root {
    --backdrop: #3a3a3a;
    --card: #fbfbfa;
    --ink: #1a1a1a;
    --muted: #8a8a8a;
    --muted-strong: #6f6f6f;
    --rule: #9a9a9a;
  }
  * { box-sizing: border-box; margin: 0; padding: 0; }
  html, body { width: 1200px; height: 900px; overflow: hidden; }
  body {
    background: var(--backdrop);
    font-family: "Lato", sans-serif;
    display: flex;
    flex-direction: column;
    align-items: center;
    justify-content: center;
    gap: 24px;
  }
  .card {
    position: relative;
    width: 700px;
    height: 400px;
    background: var(--card);
    box-shadow: 0 10px 30px rgba(0,0,0,.35);
  }
  .brand {
    position: absolute;
    top: 58px;
    right: 60px;
    display: flex;
    align-items: center;
    gap: 12px;
    font-weight: 900;
    color: var(--ink);
    letter-spacing: .04em;
    text-transform: uppercase;
  }
  .brand--pulp { font-size: 40px; }
  .brand--leaf { font-size: 24px; }
  .brand-dot {
    width: 22px; height: 22px;
    border: 2px solid var(--ink);
    border-radius: 50%;
  }
  .address {
    position: absolute;
    right: 60px;
    top: 150px;
    text-align: right;
    font-size: 15px;
    line-height: 1.35;
    color: var(--muted);
  }
  .contact-block {
    position: absolute;
    left: 60px;
    bottom: 48px;
  }
  .person-name {
    font-size: 20px;
    font-weight: 700;
    color: var(--ink);
  }
  .card--leaf .person-name { font-family: "Playfair Display", serif; font-size: 22px; }
  .person-title {
    font-size: 15px;
    color: var(--muted);
    margin-top: 2px;
  }
  .rule {
    width: 30px;
    height: 1px;
    background: var(--rule);
    margin: 20px 0 18px;
  }
  .contact-list { list-style: none; }
  .contact-list li {
    display: flex;
    align-items: center;
    gap: 12px;
    font-size: 16px;
    line-height: 24px;
    color: var(--muted-strong);
  }
  .contact-list svg { width: 13px; height: 13px; flex: none; }
</style>
</head>
<body>

<section class="card card--pulp">
  <div class="brand brand--pulp">PulpNova</div>
  <address class="address" style="font-style:normal">
    PulpNova<br>418 Larkmoor Ave.<br>Mirefield, IL 60999
  </address>
  <div class="contact-block">
    <p class="person-name">Tobin Varsk</p>
    <p class="person-title">Founder</p>
    <div class="rule"></div>
    <ul class="contact-list">
      <li><svg viewBox="0 0 16 16"><path d="M3 1h3l1.5 4-2 1.3a9 9 0 0 0 4.2 4.2L11 8.5l4 1.5v3a2 2 0 0 1-2 2A12 12 0 0 1 1 3a2 2 0 0 1 2-2z" fill="#333"/></svg>(555) 014-7738</li>
      <li><svg viewBox="0 0 16 16"><rect x="1" y="3" width="14" height="10" fill="none" stroke="#333" stroke-width="1.6"/><path d="M1 3l7 6 7-6" fill="none" stroke="#333" stroke-width="1.6"/></svg>hello@sippulpnova.example</li>
      <li><svg viewBox="0 0 16 16"><circle cx="8" cy="8" r="7" fill="#333"/><path d="M1 8h14M8 1c-3 3.5-3 10.5 0 14M8 1c3 3.5 3 10.5 0 14" fill="none" stroke="#fff" stroke-width="1"/></svg>www.sippulpnova.example</li>
    </ul>
  </div>
</section>

<section class="card card--leaf">
  <div class="brand brand--leaf"><span class="brand-dot"></span>Mirefield Crisp Leaf Co.</div>
  <address class="address" style="font-style:normal">
    Mirefield Crisp Leaf<br>418 Larkmoor Ave.<br>Mirefield, IL 60999
  </address>
  <div class="contact-block">
    <p class="person-name">Tobin Varsk</p>
    <p class="person-title">President</p>
    <div class="rule"></div>
    <ul class="contact-list">
      <li><svg viewBox="0 0 16 16"><path d="M3 1h3l1.5 4-2 1.3a9 9 0 0 0 4.2 4.2L11 8.5l4 1.5v3a2 2 0 0 1-2 2A12 12 0 0 1 1 3a2 2 0 0 1 2-2z" fill="#333"/></svg>(555) 014-7738</li>
      <li><svg viewBox="0 0 16 16"><rect x="1" y="3" width="14" height="10" fill="none" stroke="#333" stroke-width="1.6"/><path d="M1 3l7 6 7-6" fill="none" stroke="#333" stroke-width="1.6"/></svg>hello@mirefieldcrispleaf.example</li>
      <li><svg viewBox="0 0 16 16"><circle cx="8" cy="8" r="7" fill="#333"/><path d="M1 8h14M8 1c-3 3.5-3 10.5 0 14M8 1c3 3.5 3 10.5 0 14" fill="none" stroke="#fff" stroke-width="1"/></svg>www.mirefieldcrispleaf.example</li>
    </ul>
  </div>
</section>

</body>
</html>
```